Brightwell Support! Virtual Assistant business needs a Website

I have started an online business called "Brightwell Support". I offer all the same types of services as a typical Personal Assistant, only remotely. For example, document formatting and editing (word, powerpoint, excel etc.), email and calendar management, appointments and bookings, document creation, reports, travel and event management and so on.

I already have a logo ready to go, however I have yet to finalise the copy for the site, so if you could create the pages with pictures, and I can fill in the wording at a later date.

Target Market(s)

Anyone who is overloaded at work and needs someone to take the admin work off their hands.

Number of Pages Required

4 page

Font styles to use
Sans Serif
Script
Other font styles liked:
• Gotham Medium is used in my font

Colors

Designer to choose colors to be used in the design.

Requirements
Must have
• Home Page
• About Page
• Pricing Page
• Contact Page
Nice to have
• Pictures and a professional design, I like white space and simple design.
Should not have
• cartoons or anything unprofessional looking.

```html
<!DOCTYPE html>
<html lang="en">
<head>
<meta charset="utf-8">
<title>Brightwell Support</title>
<link href="https://fonts.googleapis.com/css2?family=Montserrat:wght@400;500;600;700&family=Open+Sans:ital,wght@0,400;0,600;0,700;1,400&display=swap" rel="stylesheet">
<style>
:root{
  --blue:#1f4fb4;
  --blue-deep:#163c92;
  --navy:#1b2f6b;
  --ink:#222;
  --muted:#8c8f99;
  --soft:#f4f5f8;
  --line:#b9c3dc;
  --white:#fff;
}
*{box-sizing:border-box;margin:0;padding:0}
html,body{width:1200px;height:3163px;overflow:hidden}
body{position:relative;background:var(--white);font-family:"Open Sans",Arial,sans-serif;color:var(--ink)}
.abs{position:absolute}
.heading{font-family:"Montserrat",Arial,sans-serif}

/* header */
.topline{left:0;top:0;width:1200px;height:4px;background:var(--blue-deep)}
.brand{display:flex;align-items:center;gap:10px;font-family:"Montserrat",Arial,sans-serif;font-weight:600;color:var(--navy);font-size:19px;letter-spacing:.5px}
.brand-dot{width:34px;height:34px;border-radius:50%;background:var(--navy)}
.site-logo{left:55px;top:18px}
.nav{top:26px;font-family:"Montserrat",Arial,sans-serif;font-weight:700;font-size:14px;color:var(--ink);letter-spacing:.5px}
.chat{left:948px;top:26px;font-size:14px;display:flex;align-items:center;gap:5px}
.btn-request{left:1015px;top:19px;width:148px;height:34px;border-radius:17px;background:var(--blue);color:var(--white);font-family:"Montserrat",Arial,sans-serif;font-weight:600;font-size:13px;display:flex;align-items:center;justify-content:center}

/* hero */
.hero-photo{left:0;top:70px;width:1200px;height:491px;background:linear-gradient(110deg,#3b3a36 0%,#6b5a4c 30%,#a38d7a 45%,#5b6478 65%,#283248 100%)}
.hero-tag{left:283px;top:114px;width:244px;height:48px;background:#5aa6ef;color:var(--white);font-family:"Montserrat",Arial,sans-serif;font-weight:700;font-size:17px;display:flex;align-items:center;justify-content:center}
.hero-tag:after{content:"";position:absolute;left:110px;bottom:-10px;border:10px solid transparent;border-top-color:#5aa6ef;border-bottom:0}
.intro{left:0;width:1200px;text-align:center}
.intro-lead{top:574px;font-size:21px;line-height:31px;color:#2a2a2a}
.intro-sub{top:637px;font-size:13px;color:var(--muted)}
.btn-outline{left:506px;top:673px;width:186px;height:36px;border:2px solid var(--blue-deep);border-radius:18px;font-family:"Montserrat",Arial,sans-serif;font-weight:700;font-size:13px;color:var(--navy);display:flex;align-items:center;justify-content:center;gap:8px}

/* products */
.products-bg{left:0;top:728px;width:1200px;height:917px;background:var(--soft)}
.section-title{left:0;width:1200px;text-align:center;font-family:"Montserrat",Arial,sans-serif;font-weight:700;font-size:23px;color:var(--ink)}
.section-title span{color:var(--blue)}
.dotted{left:53px;width:1097px;border-top:2px dotted var(--line)}
.product{width:280px;text-align:center}
.product svg{display:block;margin:0 auto}
.product h3{font-family:"Montserrat",Arial,sans-serif;font-weight:600;font-size:17px;color:var(--ink);margin-top:16px}
.product p{font-size:12.5px;line-height:21px;color:var(--muted);margin-top:12px}
.screen{left:295px;top:1375px;width:608px;height:382px;background:linear-gradient(180deg,#1f1f1f 0,#1f1f1f 22px,#f6f7f9 22px,#eef0f4 100%);box-shadow:0 12px 30px rgba(0,0,0,.25);z-index:2}

/* band */
.band{left:0;top:1645px;width:1200px;height:405px;background:radial-gradient(ellipse at 50% 40%,#2b63cf 0%,#1d4bb0 55%,#163c92 100%)}
.band-title{left:0;top:1788px;width:1200px;text-align:center;color:var(--white);font-family:"Montserrat",Arial,sans-serif;font-weight:400;font-size:36px}
.band-col{top:1862px;width:360px;text-align:center;color:var(--white)}
.band-col h4{font-family:"Montserrat",Arial,sans-serif;font-weight:700;font-size:17px}
.band-col p{font-size:12.5px;line-height:19px;margin-top:12px}

/* plans */
.plan{border:1.5px solid var(--blue-deep);text-align:center}
.plan-featured{background:#e9ecf4;border:none}
.plan-flag{left:428px;top:2168px;width:346px;height:38px;background:var(--blue-deep);color:var(--white);font-size:14px;display:flex;align-items:center;justify-content:center}
.plan h3{font-family:"Montserrat",Arial,sans-serif;font-weight:400;font-size:22px;color:#333;margin-top:24px}
.plan .platforms{font-size:14px;color:var(--muted);margin-top:12px}
.plan svg{display:block;margin:20px auto 0}
.plan .terms{font-size:13px;line-height:26px;color:var(--muted);margin-top:22px}
.plan .cta{display:flex;align-items:center;justify-content:center;width:142px;height:38px;border-radius:19px;margin:14px auto 0;background:#1c1c1c;color:var(--white);font-family:"Montserrat",Arial,sans-serif;font-weight:700;font-size:14px}
.plan-featured .cta{background:var(--blue-deep);width:106px}
.plan .trial{font-size:14px;margin-top:14px;color:#333}

/* testimonials */
.quotes-bg{left:0;top:2607px;width:1200px;height:398px;background:var(--soft)}
.quote{width:400px;font-size:12.5px;line-height:18px;font-style:italic;color:var(--muted)}
.quote cite{display:block;font-style:normal;color:#222;font-size:13px;margin-top:10px}
.quote-left{left:60px;text-align:right}
.quote-right{left:740px;text-align:left}
.avatar{width:76px;height:76px;border-radius:50%;background:linear-gradient(160deg,#c9b2a0,#6d5a4d)}
.divider-v{left:601px;top:2730px;height:230px;border-left:2px dotted var(--line)}
.divider-h{left:60px;top:2838px;width:1090px;border-top:1px solid #d3d7e2}

/* footer */
.footer-line{left:0;top:3005px;width:1200px;height:3px;background:var(--blue-deep)}
.footer-links{left:88px;top:3048px;display:flex;gap:26px;font-family:"Montserrat",Arial,sans-serif;font-weight:700;font-size:13px}
.footer-sub{top:3092px;display:flex;gap:22px;font-size:11.5px;color:#555}
.footer-logo{left:966px;top:3024px}
.bottomline{left:0;top:3157px;width:1200px;height:6px;background:var(--blue-deep)}
</style>
</head>
<body>

<header>
  <div class="abs topline"></div>
  <div class="abs brand site-logo"><span class="brand-dot"></span>BRIGHTWELL SUPPORT</div>
  <nav>
    <span class="abs nav" style="left:474px">ABOUT</span>
    <span class="abs nav" style="left:561px">PRICING</span>
    <span class="abs nav" style="left:658px">CONTACT</span>
  </nav>
  <span class="abs chat">Chat
    <svg width="16" height="14" viewBox="0 0 16 14" fill="none" stroke="#222" stroke-width="1.4"><path d="M2 2h9v6H6l-3 3V8H2z"/><path d="M11 5h3v6h-1v2l-2-2H7"/></svg>
  </span>
  <a class="abs btn-request">Request a Services</a>
</header>

<section class="hero">
  <div class="abs hero-photo" role="img" aria-label="Photo of two colleagues talking in a café while holding phones"></div>
  <div class="abs hero-tag">brightwell.example/free-trial</div>
  <p class="abs intro intro-lead">Personal Assistant’s email and calendar tools help you communicate<br>stay on top of what matters, and get things done.</p>
  <p class="abs intro intro-sub">See some of the features below and learn why businesses trust Personal Assistant’s</p>
  <a class="abs btn-outline"><svg width="10" height="12" viewBox="0 0 10 12"><path d="M0 0l10 6-10 6z" fill="#1b2f6b"/></svg>SEE HOW IT WORKS</a>
</section>

<section class="products">
  <div class="abs products-bg"></div>
  <h2 class="abs section-title" style="top:758px">Our <span>Products</span></h2>
  <div class="abs dotted" style="top:801px"></div>

  <div class="abs product" style="left:37px;top:850px">
    <svg width="62" height="62" viewBox="0 0 62 62" fill="none" stroke="#1d4bb0" stroke-width="2"><path d="M48 16A24 24 0 1 0 54 34"/><path d="M48 6v10H38"/><path d="M38 22a12 12 0 1 0 5 10"/></svg>
    <h3>Editing</h3><p>Sed ut perspiciatis unde omnis iste natus<br>error sit voluptate accusantium doloremqu.</p>
  </div>
  <div class="abs product" style="left:320px;top:850px">
    <svg width="62" height="62" viewBox="0 0 62 62" fill="none" stroke="#1d4bb0" stroke-width="2"><path d="M6 28L58 6 46 56 30 38z"/><path d="M58 6L30 38v16l8-10"/></svg>
    <h3>Email</h3><p>Nemo qui enim ipsam voluptatem quia<br>voluptas sit aspernatur aut odit aut fugit.</p>
  </div>
  <div class="abs product" style="left:600px;top:850px">
    <svg width="62" height="62" viewBox="0 0 62 62" fill="none" stroke="#1d4bb0" stroke-width="2"><rect x="6" y="10" width="50" height="46"/><path d="M6 22h50M18 4v12M44 4v12M6 33h50M6 44h50M19 22v34M31 22v34M43 22v34"/><circle cx="18" cy="16" r="10" fill="#f4f5f8"/><path d="M18 10v6h5"/></svg>
    <h3>Calendar Management</h3><p>Sed ut perspiciatis unde omnis iste natus<br>error sit voluptatem accusantium quido et.</p>
  </div>
  <div class="abs product" style="left:883px;top:850px">
    <svg width="62" height="62" viewBox="0 0 62 62" fill="none" stroke="#1d4bb0" stroke-width="2"><circle cx="31" cy="35" r="22"/><path d="M26 6h10M31 6v7M48 14l4-4M31 35l7-9"/></svg>
    <h3>Appointments</h3><p>Ut enim ad minim veniam, quis nostrud etor<br>exercitation ullamco laboris nisi ut aliquipe.</p>
  </div>

  <div class="abs product" style="left:37px;top:1042px">
    <svg width="62" height="62" viewBox="0 0 62 62" fill="none" stroke="#1d4bb0" stroke-width="2"><path d="M10 38A23 23 0 0 1 50 14"/><path d="M52 24A23 23 0 0 1 12 48"/><path d="M44 10l6 4-4 6M18 52l-6-4 4-6"/><path d="M36 24a6 6 0 0 0-10 4v14h12M22 34h12"/></svg>
    <h3>Bookings</h3><p>Sed ut perspiciatis unde omnis iste natus<br>error sit voluptate accusantium doloremqu.</p>
  </div>
  <div class="abs product" style="left:320px;top:1042px">
    <svg width="62" height="62" viewBox="0 0 62 62" fill="none" stroke="#1d4bb0" stroke-width="2"><rect x="12" y="8" width="38" height="50"/><rect x="22" y="4" width="18" height="8"/><path d="M20 22h22M20 30h22M20 38h22M20 46h14"/></svg>
    <h3>Documents Creation</h3><p>Nemo qui enim ipsam voluptatem quia<br>voluptas sit aspernatur aut odit aut fugit.</p>
  </div>
  <div class="abs product" style="left:600px;top:1042px">
    <svg width="62" height="62" viewBox="0 0 62 62" fill="none" stroke="#1d4bb0" stroke-width="2"><path d="M15 4v54M31 4v54M47 4v54"/><rect x="10" y="34" width="10" height="8" fill="#f4f5f8"/><rect x="26" y="14" width="10" height="8" fill="#f4f5f8"/><rect x="42" y="26" width="10" height="8" fill="#f4f5f8"/></svg>
    <h3>Reports</h3><p>Sed ut perspiciatis unde omnis iste natus<br>error sit voluptatem accusantium quido et.</p>
  </div>
  <div class="abs product" style="left:883px;top:1042px">
    <svg width="62" height="62" viewBox="0 0 62 62" fill="none" stroke="#1d4bb0" stroke-width="2"><path d="M8 24L32 6l22 18v30H8z"/><rect x="18" y="30" width="40" height="24" fill="#f4f5f8"/><path d="M18 38h40M24 48h10"/></svg>
    <h3>Travel &amp; Event Management</h3><p>Duis aute irure dolor in reprehenderit in ter<br>voluptate velit esse cillum dolore eu fugiat.</p>
  </div>

  <div class="abs screen" role="img" aria-label="Screenshot of a mail client showing a charity event planning document"></div>
</section>

<section class="organize">
  <div class="abs band"></div>
  <h2 class="abs band-title">Organize your world</h2>
  <div class="abs band-col" style="left:46px"><h4>Why Choose Us</h4><p>Sed ut perspiciatis unde omnis iste natus error sit voluptatem accusantium doloremque laudantium, totam rem aperiam, eaque ipsa quae ab illo inventore veritatis et quasi architecto beatae vitae dicta sunt explicabo. Nemo enim ipsam voluptatem quia voluptas.</p></div>
  <div class="abs band-col" style="left:417px"><h4>What You Get</h4><p>At vero eos et accusamus et iusto odio dignissimos ducimus qui blanditiis praesentium voluptatum deleniti atque corrupti quos dolores et quas molestias excepturi sint occaecati cupiditate non provident, similique sunt in culpa qui officia deserunt mollitia animi</p></div>
  <div class="abs band-col" style="left:794px"><h4>Careers at Brightwell Support</h4><p>Et harum quidem rerum facilis est et expedita distinctio. Nam libero tempore, cum soluta nobis est eligendi optio cumque nihil impedit quo minus id quod maxime placeat facere possimus, omnis voluptas assumenda est, omnis dolor repellendus temporibus.</p></div>
</section>

<section class="plans">
  <h2 class="abs section-title" style="top:2074px">Find a plan that’s <span>right for you.</span></h2>
  <div class="abs dotted" style="top:2117px"></div>

  <div class="abs plan" style="left:51px;top:2206px;width:348px;height:338px">
    <h3>Embedded Systems</h3><p class="platforms">POS, ATM, SCADA</p>
    <svg width="84" height="76" viewBox="0 0 84 76" fill="none" stroke="#1d4bb0" stroke-width="2.4"><rect x="26" y="4" width="50" height="50" rx="4"/><rect x="16" y="14" width="50" height="50" rx="4" fill="#fff"/><rect x="6" y="24" width="50" height="50" rx="4" fill="#fff"/></svg>
    <p class="terms">Requires annual commitment<br>Team Licenses available</p>
    <a class="cta">CHOOSE PLAN</a>
  </div>

  <div class="abs plan plan-featured" style="left:428px;top:2168px;width:346px;height:397px;padding-top:38px">
    <h3>Enterprise Network</h3><p class="platforms">Desktop, Server, Laptop</p>
    <svg width="110" height="76" viewBox="0 0 110 76" fill="none" stroke="#1d4bb0" stroke-width="2.4"><rect x="18" y="4" width="74" height="50" rx="3"/><path d="M8 60h94v6H8z"/><rect x="2" y="34" width="20" height="38" rx="3" fill="#e9ecf4"/><rect x="84" y="28" width="24" height="44" rx="3" fill="#e9ecf4"/></svg>
    <p class="terms">Requires annual commitment<br>Team Licenses available</p>
    <a class="cta">BUY NOW</a>
    <p class="trial">Free Trial &gt;</p>
  </div>
  <div class="abs plan-flag">Best Value</div>

  <div class="abs plan" style="left:801px;top:2206px;width:349px;height:338px">
    <h3>Cloud Platforms</h3><p class="platforms">Nimbus Cloud, Stratus Hub</p>
    <svg width="84" height="76" viewBox="0 0 84 76" fill="none" stroke="#1d4bb0" stroke-width="2.4"><path d="M20 40a14 14 0 0 1 4-27 18 18 0 0 1 34 4 12 12 0 0 1 6 23"/><path d="M12 56a12 12 0 0 1 8-20h46a12 12 0 0 1 0 24H22"/><path d="M32 20v14M42 14v20M52 20v14"/><circle cx="32" cy="20" r="3"/><circle cx="42" cy="14" r="3"/><circle cx="52" cy="20" r="3"/></svg>
    <p class="terms">Requires annual commitment<br>Team Licenses available</p>
    <a class="cta">CHOOSE PLAN</a>
  </div>
</section>

<section class="testimonials">
  <div class="abs quotes-bg"></div>
  <h2 class="abs section-title" style="top:2632px">What <span>People Say</span></h2>
  <div class="abs divider-v"></div>
  <div class="abs divider-h"></div>

  <blockquote class="abs quote quote-left" style="top:2730px">Duis aute irure dolor in reprehenderit in voluptate velit esse cillum dolore eu fugiat nulla pariatur. Excepteur sint occaecat cupidatat non proident, sunt in culpa qui officia deserunt mollit.<cite>Owen Harper, Operations Manager</cite></blockquote>
  <div class="abs avatar" style="left:491px;top:2733px" role="img" aria-label="Portrait of Owen Harper"></div>
  <div class="abs avatar" style="left:633px;top:2733px" role="img" aria-label="Portrait of Nadia Frost"></div>
  <blockquote class="abs quote quote-right" style="top:2730px">Provident, similique sunt in culpa qui officia deserunt mollitia animi, id est laborum et dolorum fuga. Et harum quidem rerum facilis est et expedita distinctio. Nam libero tempore, cum soluta nobis.<cite>Nadia Frost, Creative Designer</cite></blockquote>

  <blockquote class="abs quote quote-left" style="top:2866px">Luis aute irure dolor in reprehenderit in pluptate velit esse cillum dolore eu fugiat nulla pariatur. Excepteur sint occaecat cupidatat non proident, sunt in culpa qui officia deserunt mollit.<cite>Clara Wynn, Manager</cite></blockquote>
  <div class="abs avatar" style="left:491px;top:2870px" role="img" aria-label="Portrait of Clara Wynn"></div>
  <div class="abs avatar" style="left:633px;top:2870px" role="img" aria-label="Portrait of Theo Marsh"></div>
  <blockquote class="abs quote quote-right" style="top:2866px">At vero eos et accusamus et iusto odio dignissimos ducimus qui blanditiis praesentium voluptatum deleniti atque corrupti quos dolores et quas molestias excepturi sint occaecati asperiores.<cite>Theo Marsh, Developer</cite></blockquote>
</section>

<footer>
  <div class="abs footer-line"></div>
  <svg class="abs" style="left:50px;top:3048px" width="16" height="16" viewBox="0 0 16 16" fill="none" stroke="#333" stroke-width="1.8"><circle cx="6.5" cy="6.5" r="5"/><path d="M10 10l5 5"/></svg>
  <nav class="abs footer-links"><span>Help &amp; Contact</span><span>Our Product</span><span>Pricing</span><span>Request a Demo</span></nav>
  <div class="abs brand footer-logo"><span class="brand-dot"></span>BRIGHTWELL SUPPORT</div>
  <nav class="abs footer-sub" style="left:53px"><span>About</span><span>Blog</span><span>Careers</span><span>Public Policy</span><span>Sitemap</span><span>People</span><span>Partners</span></nav>
  <nav class="abs footer-sub" style="left:903px"><span>© 2015 - 2016</span><span>Privacy</span><span>Legal</span><span>Feedback</span></nav>
  <div class="abs bottomline"></div>
</footer>

</body>
</html>
```